Produktdesign - Kosmetikprodukt
Zielgruppe
Damen ab 50
Aufgabenstellung
Ausgeschrieben wird ein ansprechendes und hochwertiges Produktdesign für eine neu einzuführende Creme zur Vergrößerung der weiblichen Brust.
Produktname: golden bloom
Verpackung: Weiße Tube mit Schraubverschluss
Zu verwendende Begriffe auf der Vorderseite:
- golden bloom als edler Schriftzug
- VOLUME effect
- DETOX effect
- FIRMING effect
Zu verwendende Informationen auf der Rückseite:
Mit Dreifach-Wirkkomplex....
VOLUME effect: stimuliert die Adipozytendifferenzierung, damit
funktionsfähige Adipozyten entstehen - positiver Effekt auf Volumen
DETOX effect: Kelarin aktiviert Proteasome 20S, die beschädigte
Zellen beseitigt und so die Zelltoxizität herabsetzt.
FIRMING effect: steigert die Dynamik der Fibrolasten um die Matrix
Wechselwirkungen wiederherzustellen.
- Barcode mit EAN: 4260913872145
- Inhalt: 50ml
- Made in germany
- Fendrik GmbH, Otto - Ranke - Str. 4, 54321 Kaltenbrück

```html
<!DOCTYPE html>
<html lang="de">
<head>
<meta charset="utf-8">
<title>Golden Bloom – Tube</title>
<link rel="stylesheet" href="https://fonts.googleapis.com/css2?family=Ubuntu:ital,wght@1,700&family=Arimo:ital,wght@0,400;1,400&display=swap">
<style>
  :root {
    --backdrop: #ececea;
    --tube-white: #fbfbfa;
    --tube-shade: #e3e3e1;
    --brand-brown: #7b4b34;
    --band-brown: #a98876;
    --band-text: #ffffff;
    --cap-tan: #d3a98d;
    --cap-ridge: #c4987c;
    --neck-grey: #b9b9b9;
  }
  html, body {
    margin: 0;
    padding: 0;
    width: 1200px;
    height: 3069px;
    overflow: hidden;
    background: var(--backdrop);
  }
  .canvas {
    position: relative;
    width: 1200px;
    height: 3069px;
  }
  .tube-shape {
    position: absolute;
    inset: 0;
  }
  .brand-name {
    position: absolute;
    left: 0;
    width: 1140px;
    top: 700px;
    margin: 0;
    text-align: center;
    font-family: "Ubuntu", sans-serif;
    font-weight: 700;
    font-style: italic;
    font-size: 122px;
    line-height: 132px;
    color: var(--brand-brown);
  }
  .effects {
    position: absolute;
    left: 369px;
    top: 1900px;
    margin: 0;
    padding: 0;
    list-style: none;
    font-family: "Arimo", sans-serif;
    font-size: 56px;
    line-height: 73px;
    color: var(--band-text);
  }
  .effects em {
    font-style: italic;
  }
</style>
</head>
<body>
<main class="canvas">
  <svg class="tube-shape" width="1200" height="3069" viewBox="0 0 1200 3069" aria-hidden="true">
    <rect class="tube-crimp" x="180" y="172" width="812" height="112" fill="var(--tube-white)"/>
    <polygon class="tube-body" points="186,284 990,284 904,1825 873,2523 325,2523 292,1825" fill="var(--tube-white)"/>
    <line x1="180" y1="284" x2="992" y2="284" stroke="var(--tube-shade)" stroke-width="4"/>
    <polygon class="effect-band" points="292,1825 904,1825 878,2194 310,2194" fill="var(--band-brown)"/>
    <rect class="tube-neck" x="330" y="2518" width="520" height="30" fill="var(--neck-grey)"/>
    <rect class="screw-cap" x="347" y="2545" width="482" height="494" rx="18" fill="var(--cap-tan)"/>
    <g class="cap-ridges" stroke="var(--cap-ridge)" stroke-width="4">
      <line x1="380" y1="2555" x2="380" y2="2800"/>
      <line x1="415" y1="2555" x2="415" y2="2800"/>
      <line x1="450" y1="2555" x2="450" y2="2800"/>
      <line x1="485" y1="2555" x2="485" y2="2800"/>
      <line x1="520" y1="2555" x2="520" y2="2800"/>
      <line x1="555" y1="2555" x2="555" y2="2800"/>
      <line x1="590" y1="2555" x2="590" y2="2800"/>
      <line x1="625" y1="2555" x2="625" y2="2800"/>
      <line x1="660" y1="2555" x2="660" y2="2800"/>
      <line x1="695" y1="2555" x2="695" y2="2800"/>
      <line x1="730" y1="2555" x2="730" y2="2800"/>
      <line x1="765" y1="2555" x2="765" y2="2800"/>
      <line x1="800" y1="2555" x2="800" y2="2800"/>
    </g>
    <circle class="brand-dot" cx="570" cy="590" r="34" fill="var(--brand-brown)"/>
  </svg>

  <h1 class="brand-name">Golden<br>Bloom</h1>

  <ul class="effects">
    <li><em>VOLUME</em> effect</li>
    <li><em>DETOX</em> effect</li>
    <li><em>FIRMING</em> effect</li>
  </ul>
</main>
</body>
</html>
```